Word template Letterhead for Australian Law Firm

We are a small law firm based in Manly, NSW, Australia. We have had a new logo designed for us and wish to freshen up the appearance of our letterhead. We require the letterhead to be in a word document that we can type over. This will not be a ‘printed’ letterhead because we send the majority of our correspondence via email. We would like to see a few options. We have attached our previous letterhead as well as the artwork for our new logo. We like the idea of a watermark across the bottom of the letter but the watermark must stay in place and we must be able to type over it. We are open to some colour throughout the letterhead because the majority of our correspondence is sent electronically. We also use electronic signatures. I have uploaded an example of this.The letterhead must include:-1. Our address details – including our phone number, physical address, website address etc. These details can be found on the copy of our previous letterhead;2. ABN Number;3. The words ‘Brevicor (NSW) Pty Ltd ACN 482 731 058 trading as Shipton & AssociatesLiability limited by a scheme approved under Professional Standards Legislation. The letterhead does not need to include the names and qualifications of the people working at the firm. Thank you.

Target Market(s)

Clients and other parties

Industry/Entity Type

Law Firm

Font styles to use
Other font styles liked:
• raleway, montserrat

Colors

Designer to choose colors to be used in the design.

Requirements
Must have
• Certain wording - please see project description.
• Must be a word document and must be able to type over the watermark etc.
Nice to have
• Watermark at the bottom of the letter.

```html
<!DOCTYPE html>
<html lang="en">
<head>
<meta charset="utf-8">
<title>Kervell &amp; Associates Letterhead</title>
<link href="https://fonts.googleapis.com/css2?family=Carlito:wght@400;700&family=Abel&family=Raleway:wght@700&display=swap" rel="stylesheet">
<style>
  :root {
    --navy: #022361;
    --brand: #3d4a9c;
    --ink: #1a1a1a;
    --gold: #fec000;
    --sig-tone: #eeeeee;
    --badge: #1b1b1b;
  }
  * { margin: 0; padding: 0; box-sizing: border-box; }
  html, body { width: 848px; height: 1200px; overflow: hidden; background: #fff; }
  .letter {
    position: relative; width: 848px; height: 1200px; overflow: hidden;
    font-family: "Carlito", "Calibri", sans-serif; color: var(--ink);
  }
  .top-band { position: absolute; left: 0; top: 0; width: 848px; height: 31px; background: var(--navy); }
  .firm-name {
    position: absolute; left: 99px; top: 196px; display: flex; align-items: center; gap: 10px;
    font-family: "Raleway", sans-serif; font-weight: 700; font-size: 17px; letter-spacing: 1.5px; color: var(--brand);
  }
  .firm-name .dot { width: 12px; height: 12px; border-radius: 50%; background: var(--brand); }
  .contact {
    position: absolute; right: 108px; top: 128px; text-align: right;
    font-family: "Abel", sans-serif; font-size: 11.5px; line-height: 1;
  }
  .contact p { margin-bottom: 9px; }
  .contact .gap { margin-bottom: 18px; }
  .contact .web { font-family: "Carlito", sans-serif; font-weight: 700; font-size: 11.5px; letter-spacing: .3px; }
  .refs { position: absolute; left: 74px; top: 296px; font-family: "Abel", sans-serif; font-size: 10px; }
  .refs p { margin-bottom: 13px; }
  .date { position: absolute; right: 76px; top: 354px; font-size: 12.5px; }
  .date sup { font-size: 7px; }
  .body { position: absolute; left: 59px; top: 390px; width: 720px; font-size: 12.5px; }
  .salutation { margin-bottom: 24px; }
  .subject { font-weight: 700; font-size: 14.5px; margin-bottom: 18px; }
  .body .para { line-height: 34.2px; margin-bottom: 34px; }
  .body .para:first-of-type { margin-top: 0; }
  .signoff { position: absolute; left: 59px; top: 909px; font-size: 11.5px; line-height: 20px; }
  .signoff .firm { font-family: "Abel", sans-serif; }
  .signature { position: absolute; left: 63px; top: 959px; width: 91px; height: 31px; background: var(--sig-tone); }
  .signer { position: absolute; left: 59px; top: 1010px; font-size: 13px; font-weight: 700; }
  .signer-email { position: absolute; left: 59px; top: 1032px; font-family: "Abel", sans-serif; font-size: 11.5px; }
  .accreditation { position: absolute; left: 561px; top: 951px; display: flex; align-items: center; gap: 10px; }
  .accreditation .seal { width: 52px; height: 52px; border-radius: 50%; background: var(--badge); }
  .accreditation p { font-weight: 700; font-size: 9px; line-height: 12px; letter-spacing: .2px; }
  .footer {
    position: absolute; left: 0; top: 1115px; width: 848px; height: 85px; background: var(--gold);
    text-align: center; font-size: 9px; line-height: 18px; padding-top: 18px;
  }
  .footer em { font-style: italic; }
</style>
</head>
<body>
<main class="letter">
  <div class="top-band"></div>

  <div class="firm-name"><span class="dot"></span>Kervell &amp; Associates</div>

  <address class="contact" style="font-style:normal">
    <p class="gap">SUITE 4, 28 WHARF LANE HARBOURSIDE&nbsp; NSW&nbsp; 2096</p>
    <p>Tel: (02) 9481 3607 / Fax: (02) 9481 3608</p>
    <p>E-mail: reception@brevicorlaw.com.au&nbsp; ABN: 63 482 731 058</p>
    <p class="web">www.kervellassociates.com.au</p>
  </address>

  <div class="refs">
    <p>OUR REF: HM:CLR:7935</p>
    <p>YOUR REF: Tom Ardley</p>
  </div>

  <p class="date">15<sup>TH</sup> September 2019</p>

  <section class="body">
    <p class="salutation">Dear Sir/ Madam,</p>
    <h1 class="subject">RE: LETTERHEAD</h1>
    <p class="para">A letterhead is the heading at the top of a sheet of letter paper (stationery).<br>
    That heading usually consists of a name and an address, and a logo or corporate design, and sometimes a background pattern. The term "letterhead" is often used to refer to the whole sheet imprinted with such a heading. Many companies and individuals prefer to create a letterhead template in a word processor or other software application.</p>
    <p class="para">This generally includes the same information as pre-printed stationery but without the additional costs involved. Letterhead can then be printed on stationery (or plain paper) as needed on a local output device or sent electronically. That heading usually consists of a name and an address, and a logo or corporate design, and sometimes a background pattern. The term "letterhead" is often used to refer to the whole sheet imprinted with such a heading.</p>
    <p class="para">The term "letterhead" is often used to refer to the whole sheet imprinted with such a heading. Many companies and individuals prefer to create a letterhead template in a word processor or other software application.</p>
  </section>

  <div class="signoff">
    <p>Yours faithfully</p>
    <p class="firm">KERVELL &amp; ASSOCIATES</p>
  </div>
  <div class="signature" role="img" aria-label="Electronic handwritten signature"></div>
  <p class="signer">HELEN MARSH</p>
  <p class="signer-email">Direct Email: helen@brevicorlaw.com.au</p>

  <div class="accreditation">
    <span class="seal" role="img" aria-label="Accreditation seal"></span>
    <p>ACCREDITED SPECIALIST<br>FAMILY LAW</p>
  </div>

  <footer class="footer">
    <p>Brevicor (NSW) Pty Ltd ACN 482 731 058 trading as Kervell &amp; Associates</p>
    <p><em>Liability limited by a scheme approved under Professional Standards Legislation. Legal practitioners at</em></p>
    <p><em>Brevicor (NSW) Pty Ltd are members of the scheme.</em></p>
  </footer>
</main>
</body>
</html>
```